Fantasy Sports Template(s) for Marketing and Broadcast

We are a fantasy sports company doing "Pick em" style Fantasy - The fantasy system is directly connected to live sports productions such as webcasts from trelvix.com

www.kolbirax.com

We are looking for 3 templates for Social and Show production

3 separate files, similar in design

1) HOW TO JOIN KOLBIRAX TEMPLATE
- PSD Layered FIle
- Join by alsdkjflskdlfkjalskdjf
- Pick using our iPhone or Tessaly blah blah blah
- Win massive prizes with quick and easy fantasy!
- Emphasis on iPhone based image/example (you can find our application on the Orvane store or Tessaly store for example screenshots to be placed in an iphone image)

Example: https://cdn1.pravenstu.com/uploads/a81c37e920f4b6d15e0a9c7724b3f8d06e5a1c94b27d3f0e8c6a5b19d4e72f03_large

2) PRIZES ANNOUNCMENT FOR KOLBIRAX TEMPLATE
- PSD File
- 3 Placeholders with editable text layers for 1st,2nd,3rd
- Again emphasis on an iphone placeholder image - we are a mobile application. we want to emphasize that.

Similar design example

3) - LIVE BROADCAST TEMPLATE FOR KOLBIRAX

During a broadcast (1920x1080 image) we need to display

1) The current live stream (1920x1080) picture in picture
2) The top 10 users stream (Simply create placeholders for text, end graphic just needs to be blank, the data will be placed manually)
3) Fan predictions in the match up (see graphic)
4) General branding for kolbirax
5) Placeholder for up to 4 sponsor logos "brought to you by"

Please let me know if you need any help, looking forward to working with you all!

Reason: I was promised 50 designs ... i have 10.

Target Market(s)

Fantasy Sports

Industry/Entity Type

It Company

Font styles to use
Sans Serif

Colors
ec1f27
ffffff
9d9d9d
5c5c5c
333333
000000

Requirements
Must have
• Emphasis on iPhone display designs (show an iphone with an image in it) See examples
Nice to have
• Red/Black/Grey/White
• DO NOT USE MY CURRENT FILES IN YOUR DESIGN - I'm looking for a complete redesign. The logo can stay.
Should not have
• Should be SUPER SIMPLE - Immediate reactions

```html
<!DOCTYPE html>
<html lang="en">
<head>
<meta charset="utf-8">
<title>Kolbirax – Winners</title>
<link href="https://fonts.googleapis.com/css2?family=Open+Sans:wght@700;800&family=Roboto+Condensed:ital,wght@1,700&family=Nunito:wght@900&family=Roboto:wght@400&display=swap" rel="stylesheet">
<style>
  :root {
    --red: #ec1f27;
    --band-red: #dc2a2a;
    --deep-red: #8e0c1c;
    --glow: #ec6a3c;
    --white: #ffffff;
    --label-pink: #ea9593;
    --tab-first: rgba(240, 150, 150, 0.55);
    --tab-second: rgba(110, 30, 35, 0.55);
    --tab-third: rgba(75, 15, 25, 0.8);
    --fold: #333333;
    --stage-light: rgba(157, 157, 157, 0.55);
    --stage-dark: rgba(70, 40, 45, 0.85);
  }
  * { margin: 0; padding: 0; box-sizing: border-box; }
  html, body { width: 1200px; height: 675px; overflow: hidden; background: #000; }
  .canvas {
    position: relative;
    width: 1200px;
    height: 675px;
    overflow: hidden;
    background:
      radial-gradient(ellipse 560px 360px at 592px 264px, var(--glow) 0%, rgba(236,80,60,0.6) 30%, rgba(236,31,39,0) 75%),
      radial-gradient(ellipse 900px 600px at 600px 300px, var(--red) 0%, #c8122a 55%, var(--deep-red) 100%);
  }
  .crowd-glow {
    position: absolute;
    left: 0; right: 0; bottom: 0; height: 200px;
    background:
      radial-gradient(ellipse 260px 140px at 40px 200px, rgba(40,0,5,0.8), rgba(40,0,5,0)),
      radial-gradient(ellipse 260px 140px at 1160px 200px, rgba(40,0,5,0.8), rgba(40,0,5,0)),
      linear-gradient(to bottom, rgba(200,20,50,0), rgba(170,10,45,0.55));
  }
  .brand {
    position: absolute;
    left: 28px; top: 100px;
    display: flex; align-items: center; gap: 10px;
    font-family: "Open Sans", sans-serif;
    font-weight: 800;
    font-size: 34px;
    color: var(--white);
    letter-spacing: 1px;
  }
  .brand-dot { width: 18px; height: 18px; border-radius: 50%; background: var(--white); }
  .title {
    position: absolute;
    left: 0; right: 0; top: 22px;
    padding-left: 36px;
    text-align: center;
    font-family: "Open Sans", sans-serif;
    font-weight: 700;
    font-size: 66px;
    color: var(--white);
    letter-spacing: 1px;
  }
  .band {
    position: absolute;
    left: 0; top: 390px;
    width: 1200px; height: 48px;
    background: var(--band-red);
  }
  .winner { position: absolute; top: 229px; width: 208px; }
  .winner--first { left: 82px; }
  .winner--second { left: 462px; }
  .winner--third { left: 870px; }
  .photo-card { display: block; width: 208px; height: 155px; }
  .name-label {
    margin-top: 2px;
    height: 44px;
    background: var(--label-pink);
    color: var(--white);
    font-family: "Roboto Condensed", sans-serif;
    font-style: italic;
    font-weight: 700;
    font-size: 26px;
    text-align: center;
    line-height: 44px;
  }
  .prize-tab {
    width: 184px; height: 64px;
    border-radius: 0 0 8px 8px;
    color: var(--white);
    font-family: "Nunito", sans-serif;
    font-weight: 900;
    display: flex; align-items: flex-end; justify-content: center;
    padding-bottom: 6px;
    line-height: 1;
  }
  .winner--first .prize-tab { margin-left: 12px; background: var(--tab-first); }
  .winner--second .prize-tab { margin-left: 15px; background: var(--tab-second); }
  .winner--third .prize-tab { margin-left: 12px; background: var(--tab-third); }
  .place { font-size: 40px; }
  .winner--first .place { font-size: 58px; }
  .ordinal { font-size: 17px; align-self: flex-start; margin-top: 10px; margin-right: 8px; }
  .winner--first .ordinal { margin-top: 4px; margin-right: 14px; }
  .prize-word { font-size: 30px; }
  .stage {
    position: absolute; left: 0; bottom: 0;
    width: 1200px; height: 51px;
  }
  .app-note {
    position: absolute;
    left: 238px; width: 724px; bottom: 0; height: 51px;
    text-align: center;
    line-height: 48px;
    font-family: "Roboto", sans-serif;
    font-size: 24px;
    color: var(--white);
  }
</style>
</head>
<body>
<div class="canvas">
  <div class="crowd-glow" role="img" aria-label="Soft blurred stadium crowd in red tones"></div>

  <div class="brand"><span class="brand-dot"></span>KOLBIRAX</div>

  <h1 class="title">Winners</h1>

  <div class="band"></div>

  <div class="winner winner--first">
    <svg class="photo-card" viewBox="0 0 208 155" role="img" aria-label="Photo placeholder for first prize winner">
      <polygon points="146,11 198,11 198,61" fill="var(--fold)"/>
      <polygon points="0,0 146,0 208,62 208,155 0,155" fill="var(--white)"/>
    </svg>
    <div class="name-label">Placeholders</div>
    <div class="prize-tab"><span class="place">1</span><span class="ordinal">st</span><span class="prize-word">Prize</span></div>
  </div>

  <div class="winner winner--second">
    <svg class="photo-card" viewBox="0 0 208 155" role="img" aria-label="Photo placeholder for second prize winner">
      <polygon points="146,11 198,11 198,61" fill="var(--fold)"/>
      <polygon points="0,0 146,0 208,62 208,155 0,155" fill="var(--white)"/>
    </svg>
    <div class="name-label">Placeholders</div>
    <div class="prize-tab"><span class="place">2</span><span class="ordinal">nd</span><span class="prize-word">Prize</span></div>
  </div>

  <div class="winner winner--third">
    <svg class="photo-card" viewBox="0 0 208 155" role="img" aria-label="Photo placeholder for third prize winner">
      <polygon points="146,11 198,11 198,61" fill="var(--fold)"/>
      <polygon points="0,0 146,0 208,62 208,155 0,155" fill="var(--white)"/>
    </svg>
    <div class="name-label">Placeholders</div>
    <div class="prize-tab"><span class="place">3</span><span class="ordinal">rd</span><span class="prize-word">Prize</span></div>
  </div>

  <svg class="stage" viewBox="0 0 1200 51">
    <polygon points="30,0 1170,0 1200,51 0,51" fill="var(--stage-light)"/>
    <rect x="238" y="0" width="724" height="51" fill="var(--stage-dark)"/>
  </svg>
  <p class="app-note">you can find our mobile app on the Orvane store or Tessaly store</p>
</div>
</body>
</html>
```